Book Marketing Site for authors needs redesign

I need a site redesign for the site www.quornvale.com I would like to have it designed/created in Wordpress so that I can change/edit the text as necessary. Ideally, we can simplify the site so that Wordpress updates do not impact the functionality of the site.

I want to continue to use the Quornvale logo, so I would like the site to work the existing logo. I am also planning to add the tag line Reader Outreach Made Plain so please incorporate the tag line with the logo and the site.

Initially, I would like to see the page design template and then once that is approved, you to program the site. Wherever, I have indicated that we would capture email addresses; I would like to set it up so that the names are captured in my Mailwick Hub account.

Below are the elements that will need to be part of the site:
_______

Elements that should be above the fold:

• Chirpnet, Friendwall, Orbix+ and Workloop buttons with the copy “Connect with Dorothy”
o
• The copy “Sign up for our free newsletter and receive our list of Top Chirpnet Tips for Authors Free!” with a box to enter email address. The button should say “Go” not "Submit".
• A space/box for a short, 10-15 word testimonials. The testimonials will need to change from page to page.

Nav Bar/sub nav bars

Services
Packages Speaking Testimonials
FAQ
-
About Us
Speaking
-
Resources
-
Our clients
Testimonials
-
Blog
-
Contact Us

Home page
• Should have the following copy:
High Impact Book Marketing for Authors

Quornvale Marketing is book marketing service that that provides authors with an effective,
affordable approach to marketing their book.

We provide marketing coaching and consulting services that accelerate book sales, target your ideal reader and develop a community of fans that will promote your book for you.

Using high impact, low cost marketing strategies, we will develop a book marketing strategy that achieves your goals and accommodates your budget

Do you
• Want to be a best selling author, but need someone to show you the way

• Wonder what is the secret to achieving high book sales?

• Worry that you aren’t doing the right things to ensure that your book is a success?

• Need someone to help keep your spirits up and maintain momentum?

• Please put the following copy in a box at the bottom of the copy.
o Are you ready for results? Call now for a free consultation 214-555-0183

Services Page
• Copy to come

Packages Page

FAQ Page
• Same as existing site

About page
• Same as existing site

Speaking Page

Speaking

If you’re looking to create an exceptional program that your attendees won’t be able to stop talking about, you have found it!

Dorothy Pellam, a leader in book marketing, has ability to make sophisticated internet concepts easy and accessible, and the unique ability to not only to inform, but also to inspire. Her presentations leave participants with tangible, actionable ideas proven to increase book sales.

Dorothy's talks combine practical step-by-step instructions, real-life examples with plenty of humor. Call 214-555-0183 to book her now!

Dorothy’s most popular talks:

• Unlocking the Power of Pagehive
• How to Simplify Social Media
• The Ideal Author Website
• Bazario: What You Need to Know to Succeed

Resources page
• Same as existing site

Clients
• Same as existing site

Testimonials
• I would like to be able to put a image of book cover next to the testimonial on this page.

Blog page
• Please add the following elements:
• A way to sign up for the blog via RSS
o Each blog article should have a way to Friendwall like, Tweet, O+, Pokk and Trundlefind the article

Contact us page
• Same as existing site

Site Map
• Please make sure to include a site map.

Chirpnet and Friendwall headers
• Please provide both with consistent branding.

Target Market(s)

Clients are both traditionally and indie published authors trying to be the next M.K. Orwin!

Industry/Entity Type

Marketing

Requirements
Must have
• Elements that should be above the fold:

o

```html
<!DOCTYPE html>
<html lang="en">
<head>
<meta charset="utf-8">
<title>Quornvale Marketing – High Impact Book Marketing for Authors</title>
<link rel="stylesheet" href="https://fonts.googleapis.com/css2?family=PT+Sans:wght@400;700&display=swap">
<style>
:root{
  --green:#5ba33b;
  --green-text:#5a9e2f;
  --blue:#1e6aa8;
  --nav-top:#2a79bd;
  --nav-bottom:#0f4f8f;
  --text:#666;
  --text-dark:#555;
  --line:#dcdcdc;
  --panel:#f2f2f2;
  --footer:#f3f3f3;
  --social:#8a9bb0;
}
*{box-sizing:border-box;margin:0;padding:0}
html,body{width:1200px;height:1133px;overflow:hidden;background:#fff}
body{font-family:"PT Sans",Arial,sans-serif;color:var(--text)}
.page{position:relative;width:1150px;height:1086px;transform:scale(1.04348);transform-origin:0 0}
.abs{position:absolute}
.top-rule{left:0;top:0;width:1150px;height:4px;background:var(--green)}
.brand{left:90px;top:48px;display:flex;align-items:center;gap:12px}
.brand-mark{width:22px;height:22px;background:var(--blue)}
.brand-name{font-size:30px;font-weight:700;color:var(--blue);letter-spacing:1px}
.brand-sub{font-size:30px;font-weight:700;color:var(--blue)}
.call{right:87px;top:22px;font-size:22px;font-weight:700;color:#5a5a5a}
.connect{right:87px;top:89px;display:flex;align-items:center;gap:12px;font-size:12.5px;color:#888}
.social{display:flex;gap:12px}
.social span{width:26px;height:26px;background:var(--social);border-radius:3px;display:block}
.nav{left:87px;top:140px;width:976px;height:50px;display:flex;background:linear-gradient(var(--nav-top),var(--nav-bottom))}
.nav a{display:flex;align-items:center;justify-content:center;color:#fff;text-decoration:none;font-size:15.5px;text-transform:uppercase;border-right:1px solid #0b3d70;border-left:1px solid #3a89cc}
.nav a.active{background:linear-gradient(#7dbb52,#4f9330);border:none}
.slider{left:87px;top:198px;width:976px;height:270px;border:1px solid #e2e2e2;background:#f4f4f4}
.slide{left:8px;top:7px;width:959px;height:254px;background:linear-gradient(90deg,#151515 0%,#3c3c3c 30%,#bdbdbd 55%,#8f8f8f 75%,#1b1b1b 100%)}
.slide-title{left:30px;top:63px;font-size:28px;font-weight:700;color:#fff}
.slide-btn{left:33px;top:102px;width:140px;height:38px;border-radius:3px;background:linear-gradient(#b5b5b5,#7d7d7d);color:#fff;font-size:16px;font-weight:700;display:flex;align-items:center;justify-content:center;border:1px solid #ccc}
.slide-arrows{left:33px;top:211px;display:flex;gap:3px}
.slide-arrows span{width:20px;height:20px;background:#fff;border:1px solid #ccc;display:flex;align-items:center;justify-content:center}
.slider-shadow{left:120px;top:468px;width:910px;height:22px;background:radial-gradient(ellipse at top,rgba(0,0,0,.14),rgba(0,0,0,0) 70%)}
h1,h2{font-weight:700;color:var(--blue)}
.intro-title{left:87px;top:507px;font-size:22px}
.intro{left:87px;top:547px;width:675px;font-size:14px;line-height:24px;text-align:justify;color:#6a6a6a}
.intro p+p{margin-top:6px}
.divider{left:87px;top:698px;width:677px;height:1px;background:var(--line)}
.do-title{left:85px;top:717px;font-size:22px}
.questions{left:88px;top:764px;list-style:none;font-size:14px;color:var(--text-dark)}
.questions li{display:flex;align-items:center;height:40px;gap:13px}
.questions li::before{content:"";width:11px;height:11px;border:1px solid #bbb;background:#f4f4f4}
.books{left:605px;top:785px;width:180px;height:120px;background:linear-gradient(135deg,#fafafa,#d7d7d7 55%,#4a76b3 56%,#e9e9e9 62%,#fff)}
.cta{left:89px;top:922px;font-size:18px;color:var(--green-text)}
.newsletter{left:800px;top:508px;width:263px;height:187px;background:var(--panel);border:1px solid #e0e0e0;border-radius:3px}
.nl-head{left:19px;top:14px;display:flex;align-items:center;gap:12px}
.nl-head h2{font-size:23px;color:var(--green)}
.nl-text{left:19px;top:55px;width:228px;font-size:13.5px;line-height:20px;color:var(--text-dark)}
.nl-form{left:20px;top:129px;width:223px;height:37px;background:#fff;border:1px solid #ddd;display:flex;align-items:center;justify-content:space-between;padding:0 4px 0 11px;font-size:13.5px;color:#888}
.go{width:28px;height:28px;border-radius:50%;background:linear-gradient(#fff,#ddd);border:1px solid #ccc;display:flex;align-items:center;justify-content:center}
.testimonial{left:800px;top:714px;width:263px;height:189px;border:1px solid #ddd;border-radius:3px;background:linear-gradient(#fff 60%,#f1f1f1)}
.testimonial h2{position:absolute;left:0;top:16px;width:100%;text-align:center;font-size:22px;color:var(--green)}
.testimonial blockquote{position:absolute;left:20px;top:54px;width:223px;text-align:center;font-size:14px;line-height:22px;color:var(--text-dark)}
.tail{left:1020px;top:901px}
.author{left:970px;top:921px;font-size:15px;color:var(--blue)}
.footer{left:0;top:971px;width:1150px;height:115px;background:var(--footer);border-top:1px solid var(--line)}
.foot-links{left:87px;top:29px;font-size:14.5px;color:#666;word-spacing:2px}
.copyright{left:87px;top:63px;font-size:14px;color:#666;word-spacing:2px}
.foot-connect{left:925px;top:29px;font-size:14px;color:#666}
.foot-social{left:926px;top:51px}
</style>
</head>
<body>
<div class="page">
  <div class="abs top-rule"></div>

  <header>
    <div class="abs brand"><span class="brand-mark"></span><span class="brand-name">Quornvale Marketing</span></div>
    <div class="abs call">Call us : 214-555-0183</div>
    <div class="abs connect">Connect with Dorothy :
      <div class="social" role="img" aria-label="Friendwall, Chirpnet, Workloop and Orbix+ buttons"><span></span><span></span><span></span><span></span></div>
    </div>
    <nav class="abs nav">
      <a class="active" href="#" style="width:124px">Home</a>
      <a href="#" style="width:144px">Services</a>
      <a href="#" style="width:140px">About Us</a>
      <a href="#" style="width:142px">Resources</a>
      <a href="#" style="width:153px">Our Clients</a>
      <a href="#" style="width:119px">Blog</a>
      <a href="#" style="width:154px">Contact Us</a>
    </nav>
  </header>

  <section class="abs slider">
    <div class="abs slide" role="img" aria-label="Close-up photo of a typewriter typing the words success story">
      <div class="abs slide-title">Reader Outreach Made Plain</div>
      <div class="abs slide-btn">Get Started Now</div>
      <div class="abs slide-arrows">
        <span><svg width="8" height="10" viewBox="0 0 8 10"><path d="M6 1L2 5l4 4" fill="none" stroke="#5ba33b" stroke-width="2"/></svg></span>
        <span><svg width="8" height="10" viewBox="0 0 8 10"><path d="M2 1l4 4-4 4" fill="none" stroke="#5ba33b" stroke-width="2"/></svg></span>
      </div>
    </div>
  </section>
  <div class="abs slider-shadow"></div>

  <main>
    <h1 class="abs intro-title">High Impact Book Marketing for Authors</h1>
    <div class="abs intro">
      <p>Quornvale Marketing is book marketing service that that provides authors with an effective,affordable approach to marketing their book. We provide marketing coaching and consulting services that accelerate book sales, target your ideal reader and develop a community of fans that will promote your book for you.</p>
      <p>Using high impact, low cost marketing strategies, we will develop a book marketing strategy that achieves your goals and accommodates your budget.</p>
    </div>
    <div class="abs divider"></div>
    <h2 class="abs do-title">Do you</h2>
    <ul class="abs questions">
      <li>Want to be a best selling author, but need someone to show you the way</li>
      <li>Wonder what is the secret to achieving high book sales?</li>
      <li>Worry that you aren’t doing the right things to ensure that your book is a success?</li>
      <li>Need someone to help keep your spirits up and maintain momentum?</li>
    </ul>
    <div class="abs books" role="img" aria-label="Illustration of a row of white books with one blue book"></div>
    <p class="abs cta">Are you ready for results? Call now for a free consultation 214-555-0183</p>
  </main>

  <aside>
    <div class="abs newsletter">
      <div class="abs nl-head">
        <svg width="26" height="18" viewBox="0 0 26 18"><rect x="1" y="1" width="24" height="16" fill="#6fb445"/><path d="M1 1l12 9 12-9" fill="none" stroke="#fff" stroke-width="1.6"/></svg>
        <h2>Newsletter Signup</h2>
      </div>
      <p class="abs nl-text">Sign up for our free newsletter and receive our list of Top Chirpnet Tips for Authors Free!</p>
      <div class="abs nl-form">Enter your mail ID
        <span class="go"><svg width="10" height="12" viewBox="0 0 10 12"><path d="M3 1l5 5-5 5" fill="none" stroke="#555" stroke-width="2.2"/></svg></span>
      </div>
    </div>
    <div class="abs testimonial">
      <h2>Testimonials</h2>
      <blockquote>"Sed vitae luctus ligula, a tincidunt neque. Proin aliquet ligula non ultri cies eleifend. Aenean vulputate ipsum non orci mattis adipiscing orci nec tellus egestas."</blockquote>
    </div>
    <svg class="abs tail" width="28" height="26" viewBox="0 0 28 26"><path d="M1 0v24L26 1" fill="#f1f1f1" stroke="#ddd"/><rect x="2" y="0" width="24" height="2" fill="#f1f1f1"/></svg>
    <div class="abs author">Ansel</div>
  </aside>

  <footer class="abs footer">
    <div class="abs foot-links">Home &nbsp;| &nbsp;Services &nbsp;| &nbsp;About Us &nbsp;| &nbsp;Resources &nbsp;| &nbsp;Our clients &nbsp;| &nbsp;Blog &nbsp;| &nbsp;Contact Us &nbsp;| &nbsp;Sitemap</div>
    <div class="abs copyright">Copyright © 2013 &nbsp;Quornvale. &nbsp; All rights reserved.</div>
    <div class="abs foot-connect">Connect with Dorothy :</div>
    <div class="abs social foot-social" role="img" aria-label="Friendwall, Chirpnet, Workloop and Orbix+ buttons"><span></span><span></span><span></span><span></span></div>
  </footer>
</div>
</body>
</html>
```